Women Web Portal

We are developing an internet portal with content created by and for women in Latin America.
This portal will contain different categories focused on relevant topics for women who are at the same time mothers, lovers, workers, pet-owners, ...

We are looking for design that are at the same time uncluttered, easy-to-use and obvious, and comfy. Pastel colours, buttons using traditional fonts, large space for pictures, highlighted social elements,...

Our target being the middle-class women, we want a design that feels comfortable, real, a bit trendy and traditional, not a Tarsk & Welmore design, something women can relate to and feel comfortable enough to come back and participate.

Examples of websites:
www.dishtable.example
mujer.qelvo.example
www.cabellorinva.example
www.fourneau.example
Updates

Hi dear designers. After viewing some first drafts, I have updated the brief so you might have a better understanding of what we are looking for.

Thanks

Reason: We've been away for a while, unavailable to provide adequate feedback to the designs already sent. So we're extending the deadline in order to give time to everyone to adapt their work according to the feedback we'll be providing today.

Target Market(s)

Women between 25 and 50 years from Latin America. Mainly mothers: basically, we want women to interact with each other and with the content of the site so they create a strong community.

Advertisingly speaking, we want to have users, contents and FMCG brands to live together on this website.

Industry/Entity Type

Internet

Requirements
Must have
• Pastel colours for category tabs. Comfortable look & feel.

The design should include 3 different pages:
- Homepage
- Article page
- User profile

The page will be done in responsive design, so design should be thought to be adapted according to the browser (2 or 3 columns).

Thanks for doing it as a PSD file .

The design should also include:
- 8 category tabs
- Space for 728x90px and 300x600px advertising format.
- A relevant menu bar at the beginning of each page
Nice to have
• News feed/best content/most active comments zone: we need to bring forward content to our users so they'll be attracted to visit more pages of the website.

Small format to register (account).

Slider or any other moving objects.

Any idea that would facilitate and increase user participation
Should not have
• Actual text. please use Lorem Ipsum.

```html
<!DOCTYPE html>
<html lang="en">
<head>
<meta charset="utf-8">
<title>Women Web Portal — Homepage</title>
<link rel="stylesheet" href="https://fonts.googleapis.com/css2?family=Questrial&family=Arimo:ital,wght@0,400;0,700;1,400&display=swap">
<style>
:root{
  --ink:#555b60;
  --ink-soft:#8a8f93;
  --ink-faint:#a7abae;
  --green:#4daf2b;
  --green-dark:#3f9a22;
  --green-pale:#e4f6dc;
  --slide-green:#5cb533;
  --page-bg:#f3f8fb;
  --card-bg:#f7f6f6;
  --card-line:#e1e1e1;
  --side-bg:#e4e4e4;
  --side-line:#d4d4d4;
  --black:#050607;
  --header-art:#14324d;
  --white:#ffffff;
  --link-gold:#f2b31c;
}
*{box-sizing:border-box;margin:0;padding:0}
html,body{width:721px;height:1200px;overflow:hidden}
body{position:relative;background:linear-gradient(160deg,#ffffff 0%,var(--page-bg) 40%,#eef5f8 70%,#fafcfd 100%);font-family:"Arimo",Arial,sans-serif;color:var(--ink)}
.abs{position:absolute}
h2,h3{font-weight:400}

.top-band{left:0;top:0;width:721px;height:58px;background:var(--black);border-bottom:2px solid var(--green)}
.header-art{left:110px;top:0;width:240px;height:56px;background:linear-gradient(90deg,var(--black) 0%,var(--header-art) 50%,var(--black) 100%)}

.site-band{left:76px;top:60px;width:374px;height:48px;background:var(--green)}
.logo-block{left:76px;top:60px;width:122px;height:76px;background:linear-gradient(180deg,var(--green) 0%,var(--green-dark) 100%);border-radius:0 0 4px 4px;box-shadow:0 2px 3px rgba(0,0,0,.15)}
.logo-name{left:96px;top:77px;font-family:"Questrial",sans-serif;font-size:15px;color:#2e4a1f}
.logo-mark{left:122px;top:100px;width:14px;height:14px;border-radius:50%;background:#8fd46a}
.main-nav{left:214px;top:72px;display:flex;gap:12px}
.main-nav a{display:block;height:24px;line-height:24px;background:linear-gradient(#fff,#e6e6e6);color:#4a4a4a;font-size:11px;font-weight:700;text-decoration:none;text-align:center;border:1px solid #d5d5d5}
.nav-home{width:57px}.nav-article{width:58px}.nav-user{width:57px}

.slider{left:76px;top:150px;width:374px;height:180px;background:var(--green-pale);border:1px solid #d3ebc8;border-radius:4px;overflow:hidden}
.slide-text{left:21px;top:55px;font-family:"Questrial",sans-serif;font-size:18px;line-height:22px;color:var(--slide-green)}
.slide-photo{right:0;top:0;width:200px;height:180px;background:linear-gradient(120deg,#e9efe6 0%,#c9b8a6 45%,#d66a5b 65%,#5b4a3e 100%)}
.slider-dots{left:22px;top:158px;display:flex;gap:5px}
.slider-dots span{width:14px;height:14px;border-radius:50%;background:#b7e39e}
.slider-dots span:first-child{background:#8dd067}

.section-title{font-family:"Questrial",sans-serif;font-size:20px;color:#5a5f63}
.card{background:var(--card-bg);border:1px solid var(--card-line)}
.thumb{border:1px solid #dddddd;background:#fff;padding:2px}
.thumb div{width:100%;height:100%}
.story{font-size:8.4px;line-height:10.5px;color:var(--ink-soft)}
.story p{margin-bottom:9px}
.byline{font-style:italic;font-size:7.5px;color:var(--ink-faint);margin-bottom:8px}
.meta{font-style:italic;font-size:7.5px;color:var(--ink-faint);display:flex;align-items:center;gap:3px}

.gallery-card{background:#fff;border:1px solid var(--card-line)}
.gallery-card .pic{margin:3px;height:132px}
.gallery-card .caption{padding:10px 4px;font-size:8.5px;color:var(--ink-faint);border-top:1px solid var(--card-line)}

.sidebar{left:456px;top:60px;width:192px;height:648px;background:var(--side-bg);border:1px solid var(--side-line)}
.side-title{font-family:"Questrial",sans-serif;font-size:19px;color:#5a5f63}
.social-btn{width:174px;height:40px;background:linear-gradient(#fafafa,#e9e9e9);border:1px solid #d9d9d9;display:flex;align-items:center;gap:12px;padding-left:14px;font-family:"Questrial",sans-serif;font-size:15px;color:var(--link-gold)}
.social-btn i{width:20px;height:20px;background:#7a8da3;display:block}
.social-btn.chirp i{border-radius:50%;background:#6ab6e4}
.ad{width:174px;border:1px solid #cfcfcf}
.fan-box{left:466px;top:542px;width:174px;height:150px;background:#fff;border:1px solid #d2d2d2}
.fan-box h3{height:24px;line-height:24px;background:#ececec;text-align:center;font-family:"Questrial",sans-serif;font-size:11.5px;color:#555;border-bottom:1px solid #dcdcdc}

.footer-band{left:76px;top:1116px;width:572px;height:48px;background:var(--green);border-radius:5px 5px 0 0}
.footer-nav{left:89px;top:1139px;font-size:8.5px;color:#fff;font-weight:700}
.bottom-band{left:0;top:1164px;width:721px;height:36px;background:var(--black)}
.copyright{left:0;top:1182px;width:721px;text-align:center;font-size:6.5px;color:#8d8d8d}
</style>
</head>
<body>
<div class="abs top-band"></div>
<div class="abs header-art" role="img" aria-label="Abstract blue light artwork for the header band"></div>

<header>
  <div class="abs site-band"></div>
  <div class="abs logo-block"></div>
  <div class="abs logo-name">Your Logo</div>
  <div class="abs logo-mark"></div>
  <nav class="abs main-nav">
    <a class="nav-home" href="#">home</a>
    <a class="nav-article" href="#">article</a>
    <a class="nav-user" href="#">user</a>
  </nav>
</header>

<section class="abs slider">
  <div class="abs slide-photo" role="img" aria-label="Photo of a woman in sportswear listening to music on her phone"></div>
  <p class="abs slide-text">Women who are<br>at the same time<br>mothers, lovers,<br>workers,...</p>
  <div class="abs slider-dots"><span></span><span></span><span></span><span></span></div>
</section>

<h2 class="abs section-title" style="left:76px;top:346px">living beyond</h2>
<article class="abs card" style="left:76px;top:374px;width:374px;height:137px">
  <div class="abs thumb" style="left:9px;top:17px;width:87px;height:94px"><div role="img" aria-label="Photo of a smiling woman" style="background:linear-gradient(160deg,#fafafa 0%,#d9b7a0 45%,#5a2f3c 100%)"></div></div>
  <div class="abs story" style="left:111px;top:17px;width:250px">
    <p>Our target being the middle-class women, we want a design that feels comfortable, real, a bit trendy and traditional, not a Tarsk &amp; Welmore design</p>
    <p>Our target being the middle-class women, we want a design that feels comfortable, real, a bit trendy and traditional, not a Tarsk &amp; Welmore design</p>
    <div class="byline">By Lorena</div>
    <div class="meta">ABC &nbsp;| Know a woman? <svg width="6" height="6" viewBox="0 0 6 6"><path d="M0 0L6 3L0 6Z" fill="#a7abae"/></svg></div>
  </div>
</article>

<h2 class="abs section-title" style="left:76px;top:524px">faith</h2>
<article class="abs card" style="left:76px;top:554px;width:374px;height:136px">
  <div class="abs thumb" style="left:9px;top:16px;width:87px;height:94px"><div role="img" aria-label="Photo of a woman in a business suit" style="background:linear-gradient(160deg,#fafafa 0%,#d7b49a 40%,#2e3038 100%)"></div></div>
  <div class="abs story" style="left:111px;top:16px;width:250px">
    <p>Our target being the middle-class women, we want a design that feels comfortable, real, a bit trendy and traditional, not a Tarsk &amp; Welmore design</p>
    <p>Our target being the middle-class women, we want a design that feels comfortable, real, a bit trendy and traditional, not a Tarsk &amp; Welmore design</p>
    <div class="byline">By Lorena</div>
    <div class="meta">ABC &nbsp;| Know a woman? <svg width="6" height="6" viewBox="0 0 6 6"><path d="M0 0L6 3L0 6Z" fill="#a7abae"/></svg></div>
  </div>
</article>

<figure class="abs gallery-card" style="left:76px;top:727px;width:181px;height:165px">
  <div class="pic" role="img" aria-label="Photo of a woman kneeling on a grass field" style="background:linear-gradient(180deg,#b8c7c9 0%,#8aa05a 35%,#6d8a3e 70%,#6b3a48 100%)"></div>
  <figcaption class="caption">Marta Solis</figcaption>
</figure>
<figure class="abs gallery-card" style="left:266px;top:727px;width:184px;height:165px">
  <div class="pic" role="img" aria-label="Photo of a woman standing against a wooden wall" style="margin-left:32px;width:118px;background:linear-gradient(180deg,#7a4a3a 0%,#5a3a32 45%,#2c2f3e 100%)"></div>
  <figcaption class="caption">Marta Solis</figcaption>
</figure>

<h2 class="abs section-title" style="left:76px;top:901px">parenting</h2>
<article class="abs card" style="left:76px;top:928px;width:374px;height:138px">
  <div class="abs" role="img" aria-label="Photo of a child feeding pigeons in a square" style="left:14px;top:21px;width:115px;height:86px;background:linear-gradient(160deg,#9a9a96 0%,#6f6d6a 45%,#b44a6a 65%,#7b7770 100%)"></div>
  <div class="abs story" style="left:138px;top:20px;width:226px">
    <p>Our target being the middle-class women, we want a design that feels comfortable, real, a bit trendy and traditional, not a Tarsk &amp; Welmore design</p>
    <p>Our target being the middle-class women, we want a design that feels comfortable, real, a bit trendy and traditional, not a Tarsk &amp; Welmore design</p>
    <div class="byline">By Lorena</div>
    <div class="meta">ABC &nbsp;| Know a woman? <svg width="6" height="6" viewBox="0 0 6 6"><path d="M0 0L6 3L0 6Z" fill="#a7abae"/></svg></div>
  </div>
</article>

<aside class="abs sidebar"></aside>
<h2 class="abs side-title" style="left:466px;top:89px">Follow Us</h2>
<a class="abs social-btn" style="left:466px;top:121px">
  <i></i>Friendloop
</a>
<a class="abs social-btn chirp" style="left:466px;top:167px">
  <i></i>Chirpline
</a>
<h2 class="abs side-title" style="left:466px;top:233px">Advertisement</h2>
<div class="abs ad" role="img" aria-label="Web design agency advertisement banner" style="left:466px;top:265px;height:118px;background:linear-gradient(135deg,#e3f3fb 0%,#bfe4f4 50%,#ffffff 100%)"></div>
<div class="abs ad" role="img" aria-label="Sale advertisement banner with up to 35% off" style="left:466px;top:396px;height:119px;background:linear-gradient(135deg,#f5c1cf 0%,#e8507a 40%,#f7d34a 75%,#f3e9c8 100%)"></div>
<div class="abs fan-box"><h3>Find us on Friendloop</h3></div>

<footer>
  <div class="abs footer-band"></div>
  <div class="abs footer-nav">home | article | User | terms &amp; condition | privacy policy</div>
  <div class="abs bottom-band"></div>
  <div class="abs copyright">Copyright All Right Reserved 2012-14</div>
</footer>
</body>
</html>
```